Detail Shop Business card design

i need a business card design for my new detailing company called 'Brenner's Detail Shop'. i want an all black and white design . simple, direct and to the point. i want the designer to choose a fitting font to match the logothe front should have logo, address, phone and email and the back side should have a slogan and text indicating that we offer services on anything including cars, trucks, motorcycles and RVs. slogan will read "we take pride in your ride"
maybe also very small on the back side the IG icon with Brenners_Detail_Shop

phone 482.615.7734
address 7384 E Harlow Ave
Spokane WA 99342
email: BrennersDetail@quorvail.com

Target Market(s)

all ages , auto enthusiasts

Industry/Entity Type

Automotive

Contact Information for Business Card

the front should have logo, address, phone and email and the back side should have a slogan and text indicating that we offer services on anything including cars, trucks, motorcycles and RVs. slogan will read "we take pride in your ride"

phone 482.615.7734
address 7384 E Harlow Ave
Spokane WA 99342

Colors
000000
ffffff

Requirements
Must have
• bold font and very simple design with good spacing
Nice to have
• anything creative from the designer indicating we service any types of vehicles
Should not have
• any colors ,

```html
<!DOCTYPE html>
<html lang="en">
<head>
<meta charset="utf-8">
<title>Brenner's Detail Shop – Business Card</title>
<link rel="stylesheet" href="https://fonts.googleapis.com/css2?family=Lora:ital,wght@0,400;0,700;1,400&family=Montserrat:wght@500;600&display=swap">
<style>
  :root {
    --page: #ffffff;
    --card: #0b0b0b;
    --band: #141414;
    --ink: #ffffff;
    --muted: #bdbdbd;
  }
  * { box-sizing: border-box; margin: 0; padding: 0; }
  html, body { width: 1200px; height: 1200px; overflow: hidden; background: var(--page); }
  .canvas { position: relative; width: 1200px; height: 1200px; }
  .card { position: absolute; background: var(--card); overflow: hidden; color: var(--ink); }
  .card--front { left: 214px; top: 106px; width: 771px; height: 443px; }
  .card--back { left: 202px; top: 649px; width: 788px; height: 450px; }

  .texture-band { position: absolute; left: 0; width: 100%; height: 52px; background: var(--band); }
  .texture-band--top { top: 0; }
  .texture-band--bottom { bottom: 0; }

  .brand-mark { position: absolute; left: 58px; top: 56px; width: 344px; height: 308px; display: flex; flex-direction: column; align-items: center; justify-content: center; gap: 18px; }
  .brand-mark__circle { width: 110px; height: 110px; border: 6px solid var(--ink); border-radius: 50%; }
  .brand-mark__name { font-family: "Lora", serif; font-weight: 700; font-size: 40px; line-height: 1.1; text-align: center; color: var(--ink); }

  .person__name { position: absolute; left: 460px; top: 50px; font-family: "Lora", serif; font-weight: 400; font-size: 48px; line-height: 1; }
  .person__title { position: absolute; left: 460px; top: 104px; font-family: "Montserrat", sans-serif; font-weight: 500; font-size: 13px; letter-spacing: -0.2px; }
  .rule { position: absolute; top: 128px; height: 3px; background: var(--ink); }
  .rule--short { left: 460px; width: 78px; }
  .rule--long { left: 552px; width: 201px; }

  .contact { position: absolute; left: 460px; display: flex; gap: 10px; align-items: flex-start; font-family: "Lora", serif; font-style: italic; font-size: 17px; line-height: 22px; }
  .contact svg { width: 15px; height: 15px; margin-top: 4px; flex: none; }
  .contact--phone { top: 155px; }
  .contact--email { top: 202px; }
  .contact--address { top: 251px; }

  .slogan { position: absolute; left: 0; right: 0; top: 170px; text-align: center; font-family: "Lora", serif; font-style: italic; font-size: 54px; line-height: 1.2; }
  .services { position: absolute; left: 0; right: 0; top: 250px; text-align: center; font-family: "Montserrat", sans-serif; font-weight: 600; font-size: 14px; letter-spacing: 3px; text-transform: uppercase; color: var(--muted); }
  .social { position: absolute; left: 20px; bottom: 18px; display: flex; align-items: center; gap: 6px; font-family: "Lora", serif; font-weight: 700; font-size: 9px; }
  .social__square { width: 18px; height: 18px; border: 2px solid var(--ink); }
  .signature { position: absolute; right: 52px; top: 358px; font-family: "Lora", serif; font-style: italic; font-size: 30px; color: var(--ink); }
</style>
</head>
<body>
<main class="canvas">
  <section class="card card--front">
    <div class="texture-band texture-band--top" role="img" aria-label="Subtle diamond pattern band"></div>
    <div class="texture-band texture-band--bottom" role="img" aria-label="Subtle diamond pattern band"></div>

    <div class="brand-mark">
      <div class="brand-mark__circle"></div>
      <div class="brand-mark__name">Brenner's<br>Detail Shop</div>
    </div>

    <h1 class="person__name">Your Name</h1>
    <p class="person__title">MANAGING DIRECTOR</p>
    <span class="rule rule--short"></span>
    <span class="rule rule--long"></span>

    <p class="contact contact--phone">
      <svg viewBox="0 0 24 24" fill="none" stroke="currentColor" stroke-width="1.5"><path d="M5 3h4l2 5-2.5 1.5a11 11 0 0 0 6 6L16 13l5 2v4a2 2 0 0 1-2 2A16 16 0 0 1 3 5a2 2 0 0 1 2-2z"/></svg>
      <span>482.615.7734</span>
    </p>
    <p class="contact contact--email">
      <svg viewBox="0 0 24 24" fill="none" stroke="currentColor" stroke-width="1.5"><path d="M3 10l9-7 9 7v10H3z"/><path d="M3 10l9 6 9-6"/></svg>
      <span>BrennersDetail@quorvail.com</span>
    </p>
    <p class="contact contact--address">
      <svg viewBox="0 0 24 24" fill="none" stroke="currentColor" stroke-width="1.5"><path d="M12 22s7-7 7-12a7 7 0 0 0-14 0c0 5 7 12 7 12z"/><circle cx="12" cy="10" r="2.5"/></svg>
      <span>7384 E Harlow Ave Spokane<br>WA 99342</span>
    </p>
  </section>

  <section class="card card--back">
    <div class="texture-band texture-band--bottom" role="img" aria-label="Subtle diamond pattern band"></div>
    <p class="slogan">“we take pride in your ride”</p>
    <p class="services">Cars · Trucks · Motorcycles · RVs</p>
    <p class="social"><span class="social__square"></span>@Brenners_Detail_Shop</p>
    <p class="signature">Brenner's</p>
  </section>
</main>
</body>
</html>
```